Tech Company requires UI design for mobile app

We need a mobile app design for a company based in Singapore called "Valdor Systems". We develop innovative Android/iOS business applications. KelmaRun - a collaboration tool targeted at SMEs that improves reporting and communication between different departments of an organisation. We would like to see designs that use the colour orange, our corporate colour. The final design should communicate clean and technology inclined design.

You are expected to recreate the icons, layout and structure without affecting the workflow.This is a workplace app for employee on mobile. The mobile app aims to empower individual employee to complete the following processes:

1. HR processes - taking attendance, timesheet, employment management to payslip)
2. Inventory management - stock taking, gift redemption and real-time stock management
3. Digital form - application for inspection, safety, procurement or request creation)
4. Job - an app that allows web portal to assign work to individual worker.
Updates

Project Deadline Extended
Reason: Received feedback to extens timeline. Cheers!

Target Market(s)

C-Executive, office employee, retail promoter, worker

Industry/Entity Type

Business

Colors

Designer to choose colors to be used in the design.

Requirements
Must have
• - Design must be neat, looks professional and perceived to be user-friendly
• - Use colour theme for each category
• - Must complement with KelmaRun logo them (already attached)
• - Have "apple" feel
• - We like the layout reference 1 & reference 2 photo. However, we prefer a better colour theme (Already Attached)
• - Please download the link for the work required
• https://files.quorvex.com/open?id=7Hq2LmPzXr4WtYb9NcKd3VfJsEa
Nice to have
• More info to follow shortly
Should not have
• - Must not be loud, flashy, dull, bored,
• - Design should not clash with Kelma Run Logo
• -

```html
<!DOCTYPE html>
<html lang="en">
<head>
<meta charset="utf-8">
<title>KelmaRun – Mobile App Screens</title>
<link href="https://fonts.googleapis.com/css2?family=Open+Sans:wght@300;400;600;700&display=swap" rel="stylesheet">
<style>
:root{
  --orange:#f07020;
  --orange-deep:#e2601a;
  --orange-soft:#f59a55;
  --ink:#333333;
  --ink-soft:#5a5a5a;
  --muted:#9a9a9a;
  --line:#d9d9d9;
  --white:#ffffff;
  --stage:#7a5a48;
  --badge:#e3262b;
}
*{box-sizing:border-box;margin:0;padding:0}
html,body{width:853px;height:1200px;overflow:hidden}
body{background:var(--stage);font-family:"Open Sans",Arial,sans-serif;color:var(--ink);position:relative}
.screens{position:absolute;left:24px;top:371px;display:flex;gap:24px}
.screen{width:252px;height:458px;background:var(--white);border-radius:14px;overflow:hidden;position:relative}
/* brand */
.brand{display:flex;align-items:center;gap:8px;font-weight:300;letter-spacing:.5px}
.brand-dot{width:12px;height:12px;border-radius:50%;background:var(--orange)}
/* splash */
.splash .brand{position:absolute;left:0;right:0;top:136px;justify-content:center;font-size:30px;color:var(--ink-soft)}
.progress{position:absolute;left:46px;width:162px;top:234px;height:4px;border-radius:2px;background:var(--white);border:1px solid var(--line)}
.progress-fill{position:absolute;right:-1px;top:-1px;height:4px;width:98px;border-radius:2px;background:var(--orange)}
/* login */
.login-hero{position:absolute;left:0;top:0;width:100%;height:174px;background:linear-gradient(160deg,var(--orange-soft),var(--orange) 55%,var(--orange-deep))}
.login .brand{position:absolute;left:0;right:0;top:68px;justify-content:center;font-size:30px;color:var(--white)}
.login .brand-dot{background:var(--white)}
.field{position:absolute;left:38px;width:175px;height:22px;border-bottom:1px solid var(--line);font-size:10px;color:var(--ink-soft);display:flex;justify-content:space-between;align-items:flex-end;padding-bottom:3px}
.forgot{position:absolute;left:0;right:0;top:334px;text-align:center;font-size:9.5px;color:var(--orange)}
.signin{position:absolute;left:67px;top:368px;width:117px;height:29px;border-radius:15px;background:var(--orange);color:var(--white);font-size:11.5px;font-weight:700;display:flex;align-items:center;justify-content:center;box-shadow:0 5px 10px rgba(240,112,32,.35)}
.footer{position:absolute;left:0;right:0;top:433px;text-align:center;font-size:7.5px;line-height:11px;color:var(--ink-soft)}
/* dashboard */
.topbar{position:absolute;left:0;top:0;width:100%;height:52px;background:var(--orange);display:flex;align-items:center;justify-content:space-between;padding:0 12px}
.topbar .brand{font-size:17px;color:var(--white);gap:6px}
.topbar .brand-dot{width:8px;height:8px;background:var(--white)}
.icon-btn{position:relative;width:18px;height:18px}
.badge{position:absolute;background:var(--badge);color:var(--white);font-size:6.5px;font-weight:700;border-radius:6px;padding:0 3px;line-height:10px;border:1px solid var(--white)}
.section-title{position:absolute;left:14px;font-size:10px;font-weight:600;color:var(--ink)}
.tile-row{position:absolute;left:14px;display:flex;gap:10px}
.tile{width:49px;height:56px;background:var(--white);border-radius:4px;box-shadow:0 2px 7px rgba(0,0,0,.13);display:flex;flex-direction:column;align-items:center;padding-top:10px}
.tile svg{width:17px;height:17px;fill:var(--orange)}
.tile-label{margin-top:5px;font-size:5.5px;line-height:7px;text-align:center;color:var(--ink-soft)}
.tabbar{position:absolute;left:0;bottom:0;width:100%;height:40px;display:flex;justify-content:space-around;align-items:center}
.tab{display:flex;flex-direction:column;align-items:center;font-size:8px;font-weight:600;color:var(--orange);position:relative;width:50px}
.tab svg{width:17px;height:17px;margin-bottom:2px}
.tab.active{color:var(--ink)}
</style>
</head>
<body>
<main class="screens">

  <section class="screen splash" aria-label="Splash screen">
    <div class="brand"><span class="brand-dot"></span>Valdor</div>
    <div class="progress"><div class="progress-fill"></div></div>
  </section>

  <section class="screen login" aria-label="Sign in screen">
    <div class="login-hero" role="img" aria-label="Server rack photograph tinted orange"></div>
    <div class="brand"><span class="brand-dot"></span>Valdor</div>
    <div class="field" style="top:196px">Company ID</div>
    <div class="field" style="top:244px">Mobile No.</div>
    <div class="field" style="top:291px">Password
      <svg width="13" height="9" viewBox="0 0 24 16"><path d="M12 0C6 0 2 5 0 8c2 3 6 8 12 8s10-5 12-8C22 5 18 0 12 0zm0 13a5 5 0 110-10 5 5 0 010 10zm0-7.5a2.5 2.5 0 100 5 2.5 2.5 0 000-5z" fill="#f07020"/></svg>
    </div>
    <div class="forgot">Forgot password ?</div>
    <div class="signin">Sign in</div>
    <div class="footer">Valdor Systems Pte Ltd<br>App Version 2.0</div>
  </section>

  <section class="screen dashboard" aria-label="Home dashboard">
    <header class="topbar">
      <div class="icon-btn">
        <svg viewBox="0 0 24 24" width="18" height="18" fill="none" stroke="#fff" stroke-width="2"><path d="M6 17V11a6 6 0 0112 0v6l2 2H4z"/><path d="M10 21h4"/></svg>
        <span class="badge" style="left:10px;top:-6px">9+</span>
      </div>
      <div class="brand"><span class="brand-dot"></span>Valdor</div>
      <div class="icon-btn">
        <svg viewBox="0 0 24 24" width="18" height="18" stroke="#fff" stroke-width="2" fill="none"><path d="M3 6h18M3 12h18M3 18h18"/><path d="M15 3v6M8 9v6M14 15v6"/></svg>
      </div>
    </header>

    <h2 class="section-title" style="top:72px">Attendance</h2>
    <div class="tile-row" style="top:96px">
      <div class="tile"><svg viewBox="0 0 24 24"><path d="M2 5h8l2 2h10v13H2z"/><circle cx="8" cy="12" r="2" fill="#fff"/><path d="M4 17c1-2 7-2 8 0z" fill="#fff"/></svg><div class="tile-label">Take<br>Attendance</div></div>
      <div class="tile"><svg viewBox="0 0 24 24"><path d="M3 5h18v16H3z"/><path d="M7 2h2v4H7zM15 2h2v4h-2z"/><path d="M8 14l3 3 5-6" stroke="#fff" stroke-width="2" fill="none"/></svg><div class="tile-label">Today</div></div>
      <div class="tile"><svg viewBox="0 0 24 24"><ellipse cx="11" cy="5" rx="8" ry="3"/><path d="M3 7c0 2 16 2 16 0v4c0 2-16 2-16 0zM3 13c0 2 16 2 16 0v4c0 3-16 3-16 0z"/><circle cx="19" cy="18" r="3"/></svg><div class="tile-label">Past Records</div></div>
      <div class="tile"><svg viewBox="0 0 24 24"><circle cx="9" cy="8" r="4"/><circle cx="16" cy="7" r="3.5"/><path d="M1 20c0-5 16-5 16 0zM14 13c5-1 9 1 9 6h-5"/></svg><div class="tile-label">Station</div></div>
    </div>

    <h2 class="section-title" style="top:184px">Sales</h2>
    <div class="tile-row" style="top:208px">
      <div class="tile"><svg viewBox="0 0 24 24"><path d="M9 6h6v4H9zM5 11h6v4H5zM13 11h6v4h-6zM1 16h6v4H1zM9 16h6v4H9zM17 16h6v4h-6z"/></svg><div class="tile-label">New<br>Redemption</div></div>
      <div class="tile"><svg viewBox="0 0 24 24"><path d="M5 2h14v20H5z"/><path d="M8 6h8M8 10h8M8 14h8M8 18h5" stroke="#fff" stroke-width="1.5"/></svg><div class="tile-label">View<br>Redemption</div></div>
      <div class="tile"><svg viewBox="0 0 24 24"><path d="M2 7h5l2-3h6l2 3h5v13H2z"/><circle cx="12" cy="13" r="4" fill="#fff"/><circle cx="12" cy="13" r="2.5"/></svg><div class="tile-label">Take<br>Photo</div></div>
      <div class="tile"><svg viewBox="0 0 24 24"><path d="M4 12h3v8H4zM9 8h3v12H9zM14 4h3v16h-3zM19 10h3v10h-3zM2 21h21v1H2z"/></svg><div class="tile-label">Sales<br>Summary</div></div>
    </div>

    <h2 class="section-title" style="top:294px">Inventory</h2>
    <div class="tile-row" style="top:318px">
      <div class="tile"><svg viewBox="0 0 24 24"><path d="M4 4h16v18H4z"/><path d="M9 2h6v4H9z"/><path d="M8 13l3 3 5-6" stroke="#fff" stroke-width="2" fill="none"/></svg><div class="tile-label">Inventory<br>Check</div></div>
      <div class="tile"><svg viewBox="0 0 24 24"><path d="M1 6h14v11H1zM15 9h5l3 4v4h-8z"/><circle cx="6" cy="18" r="2.5"/><circle cx="18" cy="18" r="2.5"/></svg><div class="tile-label">Delivery</div></div>
      <div class="tile"><svg viewBox="0 0 24 24"><path d="M4 4h16v18H4z"/><path d="M9 2h6v4H9z"/><path d="M8 11l2 2 3-3M8 17h8" stroke="#fff" stroke-width="1.5" fill="none"/></svg><div class="tile-label">New<br>Stock Take</div></div>
      <div class="tile"><svg viewBox="0 0 24 24"><path d="M2 3h5v5H2zM2 10h5v5H2zM2 17h5v5H2zM10 5h12v1.5H10zM10 12h12v1.5H10zM10 19h12v1.5H10z"/></svg><div class="tile-label">Stock<br>Take List</div></div>
    </div>

    <nav class="tabbar">
      <div class="tab active"><svg viewBox="0 0 24 24" fill="none" stroke="#333" stroke-width="2"><path d="M3 11l9-8 9 8M5 10v11h14V10"/><path d="M10 21v-6h4v6"/></svg>Home</div>
      <div class="tab"><svg viewBox="0 0 24 24" fill="none" stroke="#f07020" stroke-width="2"><path d="M3 5h18v16H3zM3 10h18M8 2v5M16 2v5"/></svg>Calendar</div>
      <div class="tab"><svg viewBox="0 0 24 24" fill="none" stroke="#f07020" stroke-width="2.2"><path d="M20 11a8 8 0 00-14-5L4 8M4 13a8 8 0 0014 5l2-2"/><path d="M4 3v5h5M20 21v-5h-5"/></svg>Sync<span class="badge" style="left:28px;top:-6px">9+</span></div>
      <div class="tab"><svg viewBox="0 0 24 24" fill="none" stroke="#f07020" stroke-width="2"><circle cx="12" cy="8" r="4.5"/><path d="M3 22c0-6 18-6 18 0z"/></svg>Profile</div>
    </nav>
  </section>

</main>
</body>
</html>
```